Plakat-Design für Tora-Unterricht einer Jüdischen Gemeinde
Zielgruppe
Wir sind die Jüdische Gemeinde.(synagogenverein Talbrück.
Wir organisieren einen Tora-Unterricht.
Zielgruppe sind Gemeindemitglieder(Männer und Frauen)die meisten aus der ehemaligen Sowjetunion, 50 Jahre aufwärts. Russischsprachig.
Die Plakate sollen in der Gemeinde hängen und so viele wie es geht ansprechen.
Aufgabenstellung
Plakat in russischer Sprache. Im folgenden steht der Text mit deutscher Übersetzung. Die Übersetzung dient nur zu Ihrer Information/Orientierung. Nur bei der Zeile mit Anführungsstrichen bleibt der deutsche Text:
Цикл лекций с раввином Элиэзер Розенфельд - Vortragsreihe von Rabbiner Elieser Rosenfeld
'Свет над морем-Licht über dem Meer'
По четвергам в 13.00 - donnerstags um 13:00 Uhr
С переводом на русский язык Светланы Мирошник - mit Übersetzung ins russische von Frau Swetlana Miroschnik
Приходите все! - Alle sind herzlich willkommen!
Вас ожидают увлека тельные уроки Торы а также интересные путешествия и экскурсии.- Euch erwarten spannende Tora Unterrichte und auch interessante Ausflüge und Besichtigung

```html
<!DOCTYPE html>
<html lang="ru">
<head>
<meta charset="utf-8">
<title>Свет над морем — цикл лекций</title>
<link rel="stylesheet" href="https://fonts.googleapis.com/css2?family=Open+Sans:wght@600;700;800&display=swap">
<style>
  :root {
    --parchment-light: #e6cfae;
    --parchment-mid: #c9a27a;
    --parchment-dark: #8e6a48;
    --water-light: #bfe0e6;
    --water-mid: #6fa7b3;
    --water-deep: #2d5562;
    --water-night: #1b3440;
    --ink: #111111;
    --white: #ffffff;
    --muted: #4c5a60;
    --sand: #c9b79a;
  }
  html, body {
    margin: 0;
    padding: 0;
    width: 848px;
    height: 1200px;
    overflow: hidden;
    background: var(--white);
  }
  .poster {
    position: relative;
    width: 848px;
    height: 1200px;
    overflow: hidden;
    font-family: "Open Sans", sans-serif;
  }
  .backdrop {
    position: absolute;
    inset: 0;
    width: 848px;
    height: 1200px;
  }
  .line {
    position: absolute;
    left: 0;
    width: 848px;
    margin: 0;
    text-align: center;
    white-space: nowrap;
  }
  .series {
    color: var(--white);
    font-weight: 800;
    font-size: 30px;
    letter-spacing: 1.5px;
    line-height: 36px;
    text-shadow: 0 1px 4px rgba(60, 35, 15, 0.55);
    left: -8px;
  }
  .series--one { top: 124px; }
  .series--two { top: 161px; }
  .title {
    top: 208px;
    left: -6px;
    color: var(--ink);
    font-weight: 700;
    font-size: 74px;
    line-height: 84px;
    letter-spacing: -0.5px;
  }
  .subtitle {
    top: 280px;
    left: -6px;
    color: var(--white);
    font-weight: 600;
    font-size: 50px;
    line-height: 60px;
    text-shadow: 0 2px 6px rgba(60, 35, 15, 0.55);
  }
  .schedule {
    top: 530px;
    left: auto;
    right: 72px;
    width: auto;
    text-align: right;
    color: var(--ink);
    font-weight: 800;
    font-size: 54px;
    line-height: 64px;
  }
  .translation {
    left: auto;
    right: 81px;
    width: auto;
    text-align: right;
    color: var(--muted);
    font-weight: 800;
    font-size: 26px;
    line-height: 34px;
  }
  .translation--one { top: 598px; }
  .translation--two { top: 636px; }
  .invite {
    top: 877px;
    left: -4px;
    color: var(--sand);
    font-weight: 800;
    font-size: 76px;
    line-height: 88px;
    letter-spacing: 5px;
    text-shadow: 0 2px 6px rgba(10, 25, 35, 0.35);
  }
  .details {
    color: var(--white);
    font-weight: 700;
    font-size: 38px;
    line-height: 46px;
    text-shadow: 0 2px 6px rgba(10, 25, 35, 0.55);
    left: -2px;
  }
  .details--one { top: 964px; }
  .details--two { top: 1011px; }
  .details--three { top: 1058px; }
</style>
</head>
<body>
  <main class="poster">
    <svg class="backdrop" viewBox="0 0 848 1200" role="img" aria-label="Старинный свиток с ивритским текстом, переходящий в блестящую морскую воду с бликами света">
      <defs>
        <linearGradient id="scrollToSea" x1="0" y1="0" x2="0" y2="1">
          <stop offset="0" stop-color="#b58c65"/>
          <stop offset="0.12" stop-color="#d8b993"/>
          <stop offset="0.3" stop-color="#e2c8a6"/>
          <stop offset="0.42" stop-color="#d9c2a6"/>
          <stop offset="0.5" stop-color="#cfe2e3"/>
          <stop offset="0.6" stop-color="#a9d0d8"/>
          <stop offset="0.72" stop-color="#6e9fab"/>
          <stop offset="0.85" stop-color="#36606c"/>
          <stop offset="1" stop-color="#1f3b47"/>
        </linearGradient>
        <radialGradient id="topShade" cx="0.15" cy="0.05" r="0.6">
          <stop offset="0" stop-color="#7a5536" stop-opacity="0.55"/>
          <stop offset="1" stop-color="#7a5536" stop-opacity="0"/>
        </radialGradient>
      </defs>
      <rect width="848" height="1200" fill="url(#scrollToSea)"/>
      <rect width="848" height="600" fill="url(#topShade)"/>
    </svg>

    <p class="line series series--one">ЦИКЛ ЛЕКЦИЙ С РАВВИНОМ</p>
    <p class="line series series--two">ЭЛИЭЗЕР РОЗЕНФЕЛЬД</p>
    <h1 class="line title">„СВЕТ НАД МОРЕМ“</h1>
    <p class="line subtitle">- Licht über dem Meer -</p>

    <p class="line schedule">По четвергам в 13.00</p>
    <p class="line translation translation--one">С переводом на русский язык</p>
    <p class="line translation translation--two">Светланы Мирошник</p>

    <p class="line invite">ПРИХОДИТЕ ВСЕ!</p>
    <p class="line details details--one">Вас ожидают увлекательные</p>
    <p class="line details details--two">уроки Торы а также интересные</p>
    <p class="line details details--three">путешествия и экскурсии.</p>
  </main>
</body>
</html>
```